Harbor Renovations- Update

I would like to have a higher end website to feature recent projects and services.
LOGO Colors are #0c539d, #daa520, black

Target Market(s)

High end clients

Industry/Entity Type

Residential and Commercial Construction

Coding

Coded - Design and coding required

Number of Pages Required

5+ page

Font styles to use
Other font styles liked:
• Bernard MT, Mongolian Balti

Colors
0054AA
0677BA
7BADD7
CADEEF
E8F1F8
FFC000
F8CF3A
FAE287
FDF2CF
FEFAEE

Requirements
Must have
• Must organize the photos by project that I will provide images and folders for, Instagram and facebook connected.
Nice to have
• Video Headers?

```html
<!DOCTYPE html>
<html lang="en">
<head>
<meta charset="utf-8">
<title>Harbor Renovations</title>
<link rel="stylesheet" href="https://fonts.googleapis.com/css2?family=Lato:wght@400;700&family=Merriweather:wght@700;900&display=swap">
<style>
:root{
  --blue:#0c539d;
  --blue-deep:#0a4a8e;
  --gold:#daa520;
  --ink:#111111;
  --text:#555555;
  --white:#ffffff;
}
*{box-sizing:border-box;margin:0;padding:0}
html,body{width:1200px;height:3475px;overflow:hidden;background:var(--white);font-family:'Lato',sans-serif;color:var(--ink)}
.page{position:relative;width:1200px;height:3475px}
.abs{position:absolute}
.serif{font-family:'Merriweather',serif;font-weight:900}
.brand{font-family:'Lato',sans-serif;font-weight:700;color:var(--blue);display:flex;align-items:center;gap:10px}
.brand .mark{width:22px;height:22px;background:var(--gold)}
.social{display:flex;gap:10px}
.social span{width:34px;height:34px;border-radius:50%;background:var(--gold);display:block}
.btn{display:flex;align-items:center;justify-content:center;border-radius:4px;font-weight:700;font-size:17px}
.btn-gold{background:var(--gold);color:var(--blue)}
.btn-blue{background:var(--blue);color:var(--white)}
.photo{border-radius:22px}
/* header */
.nav{left:325px;top:68px;width:600px;height:49px;background:var(--ink)}
.nav ul{list-style:none;display:flex;height:100%;align-items:center;font-size:16px;color:var(--white)}
.nav li{width:110px;text-align:center}
.nav li.active{background:var(--blue);clip-path:polygon(12% 0,100% 0,88% 100%,0 100%);height:100%;line-height:49px}
.callbox{left:890px;top:0;width:310px;height:117px;background:var(--blue);clip-path:polygon(30px 0,100% 0,100% 100%,0 100%)}
/* hero */
.hero{left:0;top:117px;width:1200px;height:483px;background:linear-gradient(135deg,#5a5550,#8a8377 45%,#3a332e)}
.hero h1{font-size:60px;color:var(--white);width:1200px;text-align:center;top:145px;letter-spacing:1px;text-shadow:0 3px 6px rgba(0,0,0,.4)}
.hero p{width:1200px;text-align:center;top:228px;font-size:20px;color:var(--white)}
/* about */
.about p{font-size:16px;line-height:33.5px;color:var(--text)}
.eyebrow{font-size:17px;font-weight:700;color:var(--ink)}
/* services */
.card{width:315px;height:393px;background:var(--white);border-radius:28px;overflow:hidden}
.card h3{position:absolute;left:35px;top:30px;font-size:24px;line-height:36px;font-weight:700;font-family:'Merriweather',serif}
.card p{position:absolute;left:35px;top:103px;width:260px;font-size:15px;line-height:29px;color:var(--text)}
.card .img{position:absolute;left:6px;bottom:6px;width:303px;height:185px;border-radius:0 0 24px 24px;clip-path:polygon(0 25%,100% 0,100% 100%,0 100%)}
.card .edge{position:absolute;left:0;bottom:0;width:315px;height:200px;background:var(--gold);clip-path:polygon(0 24%,100% 0,100% 2%,0 26%)}
.card .go{position:absolute;right:23px;top:176px;width:54px;height:54px;border-radius:50%;background:var(--gold);display:flex;align-items:center;justify-content:center}
.sub{width:1200px;text-align:center;font-size:17px}
.foot-nav{top:3322px;left:0;width:1200px;display:flex;justify-content:center;gap:38px;font-size:16px;color:var(--white)}
</style>
</head>
<body>
<div class="page">

<!-- header -->
<header>
  <div class="abs brand" style="left:110px;top:38px;font-size:26px"><span class="mark"></span>Harbor Renovations</div>
  <div class="abs social" style="left:513px;top:16px"><span></span><span></span><span></span><span></span></div>
  <div class="abs btn btn-blue" style="left:715px;top:14px;width:132px;height:38px;font-size:15px">Contact Us</div>
  <nav class="abs nav"><ul><li class="active">Home</li><li>About Us</li><li>Gallery</li><li>Our Process</li><li>FAQ</li></ul></nav>
  <div class="abs callbox">
    <div class="abs" style="left:48px;top:33px;width:52px;height:52px;border-radius:50%;background:var(--gold)">
      <svg width="52" height="52" viewBox="0 0 52 52"><path d="M19 16c2 0 3 4 3 5s-2 2-2 3c1 3 4 6 7 7 1 0 2-2 3-2s5 1 5 3-2 4-4 4c-8 0-15-7-15-15 0-2 1-5 3-5z" fill="#fff"/></svg>
    </div>
    <div class="abs" style="left:120px;top:35px;font-size:12px;font-weight:700;color:#fff">Call Us:</div>
    <div class="abs" style="left:120px;top:52px;font-size:24px;font-weight:700;color:#fff">(555) 014-2290</div>
  </div>
</header>

<!-- hero -->
<section class="abs hero" role="img" aria-label="Modern kitchen interior with white cabinets and stainless appliances">
  <h1 class="abs serif">HARBOR RENOVATIONS</h1>
  <p class="abs">Complete renovation projects both on time and within budget.</p>
  <div class="abs btn btn-blue" style="left:528px;top:278px;width:144px;height:43px">Get Started</div>
</section>
<svg class="abs" style="left:0;top:520px" width="1200" height="90" viewBox="0 0 1200 90">
  <polygon points="0,80 1200,60 1200,90 0,90" fill="#fff"/>
  <polygon points="0,10 600,44 0,80" fill="#daa520"/>
  <rect x="587" y="25" width="26" height="36" rx="13" fill="#fff"/>
  <rect x="596" y="31" width="8" height="18" rx="4" fill="#daa520"/>
</svg>

<!-- about -->
<section class="about">
  <div class="abs" style="left:70px;top:1035px;width:112px;height:112px;border-radius:50%;background:var(--gold)"></div>
  <div class="abs photo" style="left:105px;top:683px;width:498px;height:437px;background:#fff;box-shadow:0 4px 16px rgba(0,0,0,.2);border-radius:26px"></div>
  <div class="abs photo" role="img" aria-label="House addition under construction with grey siding and house wrap" style="left:112px;top:690px;width:484px;height:423px;background:linear-gradient(160deg,#6f6c6a,#9aa3ad 50%,#dfe3e6);border-radius:22px"></div>
  <h2 class="abs serif" style="left:659px;top:722px;font-size:44px"><span style="color:var(--blue)">ABOUT</span> US</h2>
  <p class="abs" style="left:659px;top:787px;width:440px">We acquire extensive construction experience, collaborating closely with project managers and clients. This collaboration enables us to consistently complete renovation projects both on time and within budget.</p>
  <div class="abs eyebrow" style="left:659px;top:940px">HAVE DRAWINGS? SEND THEM OVER TO</div>
  <div class="abs eyebrow" style="left:659px;top:980px">STATE LICENSE <span style="color:var(--blue)">#PA000417</span></div>
  <div class="abs btn btn-gold" style="left:659px;top:1028px;width:143px;height:44px">Read More</div>
</section>

<!-- services -->
<svg class="abs" style="left:0;top:1200px" width="1200" height="735" viewBox="0 0 1200 735">
  <polygon points="0,5 1200,65 1200,735 0,735" fill="#0c539d"/>
  <polygon points="640,35 1200,0 1200,72" fill="#daa520"/>
</svg>
<h2 class="abs serif" style="left:0;top:1312px;width:1200px;text-align:center;font-size:44px;color:#fff">OUR SERVICES</h2>
<p class="abs sub" style="top:1378px;color:#fff">Our tailored construction solutions catered to each client's unique needs and preferences.</p>

<div class="abs card" style="left:106px;top:1434px">
  <h3>RESIDENTIAL<br>CONSTRUCTION</h3>
  <p>Sed ut perspiciatis unde omnis iste nat us error sit voluptatem accusa ntium doloremque laudantium</p>
  <div class="edge"></div>
  <div class="img" role="img" aria-label="Bright kitchen with white tile and wooden shelves" style="background:linear-gradient(160deg,#efece6,#c9b69a)"></div>
  <div class="go"><svg width="18" height="18" viewBox="0 0 18 18"><path d="M4 14L14 4M6 4h8v8" stroke="#111" stroke-width="2" fill="none"/></svg></div>
</div>
<div class="abs card" style="left:443px;top:1434px">
  <h3>COMMERCIAL<br>CONSTRUCTION</h3>
  <p>Sed ut perspiciatis unde omnis iste nat us error sit voluptatem accusa ntium doloremque laudantium</p>
  <div class="edge"></div>
  <div class="img" role="img" aria-label="Commercial interior under construction" style="background:linear-gradient(160deg,#8b8f93,#4a4d50)"></div>
  <div class="go"><svg width="18" height="18" viewBox="0 0 18 18"><path d="M4 14L14 4M6 4h8v8" stroke="#111" stroke-width="2" fill="none"/></svg></div>
</div>
<div class="abs card" style="left:780px;top:1434px">
  <h3>GENERAL<br>CONSTRUCTION</h3>
  <p>Sed ut perspiciatis unde omnis iste nat us error sit voluptatem accusa ntium doloremque laudantium</p>
  <div class="edge"></div>
  <div class="img" role="img" aria-label="Installer laying hexagon floor tiles" style="background:linear-gradient(160deg,#d8c3a5,#7a6a62)"></div>
  <div class="go"><svg width="18" height="18" viewBox="0 0 18 18"><path d="M4 14L14 4M6 4h8v8" stroke="#111" stroke-width="2" fill="none"/></svg></div>
</div>

<!-- projects -->
<h2 class="abs serif" style="left:0;top:2030px;width:1200px;text-align:center;font-size:44px"><span style="color:var(--blue)">RECENT</span> PROJECTS</h2>
<p class="abs sub" style="top:2094px;color:var(--text)">Our tailored construction solutions catered to each client's unique needs and preferences.</p>
<div class="abs photo" role="img" aria-label="Laundry nook with stacked washer and dryer" style="left:111px;top:2162px;width:299px;height:380px;background:linear-gradient(160deg,#a9c4c6,#6f8f92)"></div>
<div class="abs photo" role="img" aria-label="Two-storey addition with scaffolding and house wrap" style="left:430px;top:2162px;width:658px;height:380px;background:linear-gradient(160deg,#7e8790,#d9dcdf 55%,#4f5a3e)"></div>
<div class="abs photo" role="img" aria-label="Kitchen with navy cabinets and white countertop" style="left:111px;top:2566px;width:658px;height:380px;background:linear-gradient(160deg,#cdbfb3,#2f3f5e 70%)"></div>
<div class="abs photo" role="img" aria-label="Empty room with large windows and drywall finish" style="left:790px;top:2566px;width:298px;height:380px;background:linear-gradient(160deg,#f0f0ef,#c9c9c7)"></div>
<div class="abs btn btn-gold" style="left:529px;top:2985px;width:143px;height:44px">View More</div>

<!-- footer -->
<svg class="abs" style="left:0;top:3080px" width="1200" height="395" viewBox="0 0 1200 395">
  <polygon points="0,5 1200,70 1200,395 0,395" fill="#111"/>
  <polygon points="640,35 1200,0 1200,75" fill="#daa520"/>
</svg>
<div class="abs brand" style="left:0;top:3222px;width:1200px;justify-content:center;font-size:36px"><span class="mark" style="width:30px;height:30px"></span>Harbor Renovations</div>
<nav class="abs foot-nav"><span>HOME</span><span>|</span><span>ABOUT US</span><span>|</span><span>GALLERY</span><span>|</span><span>OUR PROCESS</span><span>|</span><span>FAQ</span><span>|</span><span>CONTACT US</span></nav>
<div class="abs social" style="left:503px;top:3373px"><span style="width:40px;height:40px"></span><span style="width:40px;height:40px"></span><span style="width:40px;height:40px;background:var(--blue)"></span><span style="width:40px;height:40px"></span></div>
<p class="abs" style="left:0;top:3435px;width:1200px;text-align:center;font-size:13px;color:#fff">(C) Copyright 2024 | All Rights Reserved</p>

</div>
</body>
</html>
```